依頼詳細
人工知能(AI)というデジタルでクールなイメージと、教育というアナログで優しいイメージを合わせもった雰囲気のWebサイトを構築したいと考えています。
海外のデザイナーにたたき台となるデザインをしていただいたのですが、やはり日本のデザインとは異なるところが多くあり、日本のデザイナーさんに再度依頼しようと決めました。
他の案件と比べるとたたき台となるWebデザインや営業用のフライヤーまでそろっていますので、色やデザインの印象がつかみやすいと思います。

現ホームページもありますが、会社の内容であったりをつかみにくいため、もっとわかりやすく華やかな印象があり信頼できるページのデザインに仕上げたいと考えています。

こちらに「たたき台となる海外のデザイナーによるWebデザイン」と「日本のデザイナーによるフライヤー(完成版)」の画像がありますので、大きく参考になると思いますので、必ずすべての画像を見ていただいてから作業の開始をお願いします。
https://files.norebun.jp/share/folders/83kqpwZTRmvbhaa41xLoyy0cMEFdPZn7?usp=sharing

海外のデザイナーさんは悪くはないのですが、やはり日本のデザインとは異なり、もう少し日本らしいデザインで信頼性を確保したいと思っています。

今回はこの「トップページ」に関して作成をお願いします。
言葉に関しては後から埋めていけますので、ダミーで入れていただければと思います。

私の好きなサイトデザインを挙げておきますので、ご参考まで。
https://www.tovrex.jp/
https://mizu-lab.in/

単なるまねではなく、個性がしっかりと出ていて、求めていたデザインとなる方と一緒に理想のデザインを求めていければ幸いです。

みなさま、どうぞよろしくお願いいたします。
サイトURL
https://www.sorumina.co.jp/
ページ数
1ページ
希望イメージ
シンプル 複雑
単色 カラフル
暗い 明るい
日常 高級
遊び心 厳粛
未来的 伝統的
女性的 男性的
希望する色
青系、水色系
納品ファイル
• 高解像度JPG (.jpg)
• イラストレーター形式 (.ai)
• フォトショップ形式 (.psd)
補足説明
画像ファイルなどは詳細依頼をご確認ください。
■ 選んだ理由

依頼内容に記載した内容だけではなく、弊社のHPやインタビュー記事なども参考にしていただき、会社の方針を汲み取り、デザインに上手く反映していただいた点から選ばさせていただきました。

■ 提案者全員のお礼・コメント

この度は、既にあるデザインの再構成という一般的な依頼内容とは少し毛色が違うご依頼になってしまったにも関わらず、多数のご提案をありがとうございました。
また、ご縁がございましたら、何卒、よろしくお願いいたします。

```html
<!DOCTYPE html>
<html lang="ja">
<head>
<meta charset="utf-8">
<title>ルミエラ | AI人材が育つ</title>
<link rel="stylesheet" href="https://fonts.googleapis.com/css2?family=Noto+Serif+JP:wght@400;600;700&family=Noto+Sans+JP:wght@400;500;700&family=Lato:ital,wght@0,400;0,700;1,700&display=swap">
<style>
:root{
  --blue:#3c9bd0;
  --blue-deep:#2c7fb3;
  --sky:#8ccbdc;
  --sky-light:#e9f3f8;
  --ink:#3c4650;
  --muted:#7c8791;
  --line:#d9e3ea;
  --white:#ffffff;
  --plan:#7cb940;
  --do:#2e8fd2;
  --action:#e14a3f;
  --check:#f1b52a;
}
*{margin:0;padding:0;box-sizing:border-box}
html,body{width:1200px;height:3692px;overflow:hidden}
body{font-family:"Noto Sans JP",sans-serif;color:var(--ink);background:var(--white);position:relative}
.serif{font-family:"Noto Serif JP",serif}

/* header */
.site-header{position:absolute;top:0;left:0;width:1200px;height:80px;z-index:5}
.brand{position:absolute;left:60px;top:22px;display:flex;align-items:center;gap:10px}
.brand-dot{width:34px;height:34px;border-radius:50%;background:var(--blue)}
.brand-name{font-size:17px;font-weight:700;color:var(--blue-deep);letter-spacing:.08em}
.global-nav{position:absolute;left:580px;top:30px;display:flex;gap:8px}
.global-nav a{font-family:"Lato",sans-serif;font-size:12px;color:var(--ink);text-decoration:none;padding:5px 14px;border-radius:14px}
.global-nav a.is-active{background:var(--blue);color:var(--white)}
.btn-contact{position:absolute;left:1020px;top:26px;width:110px;height:32px;border-radius:16px;background:var(--blue);color:var(--white);font-family:"Lato",sans-serif;font-size:12px;display:flex;align-items:center;justify-content:center}

/* buttons */
.btn-more{position:absolute;width:160px;height:34px;border-radius:17px;background:var(--blue);color:var(--white);font-family:"Lato",sans-serif;font-size:11px;letter-spacing:.15em;display:flex;align-items:center;justify-content:center}
.btn-more.is-light{background:var(--white);color:var(--blue)}

/* hero */
.hero{position:absolute;top:0;left:0;width:1200px;height:600px;
  background:
   radial-gradient(circle at 8% 30%,rgba(120,200,235,.55) 0 90px,transparent 91px),
   radial-gradient(circle at 20% 12%,rgba(250,200,215,.6) 0 55px,transparent 56px),
   radial-gradient(circle at 28% 48%,rgba(200,225,120,.45) 0 40px,transparent 41px),
   radial-gradient(circle at 12% 70%,rgba(250,220,110,.5) 0 60px,transparent 61px),
   radial-gradient(circle at 86% 20%,rgba(130,205,240,.55) 0 95px,transparent 96px),
   radial-gradient(circle at 74% 10%,rgba(250,190,210,.55) 0 45px,transparent 46px),
   radial-gradient(circle at 95% 60%,rgba(250,220,110,.5) 0 70px,transparent 71px),
   radial-gradient(circle at 78% 55%,rgba(190,225,130,.45) 0 38px,transparent 39px),
   radial-gradient(circle at 62% 75%,rgba(140,210,240,.35) 0 30px,transparent 31px),
   linear-gradient(#fbfdfe,#f1f6f9)}
.hero-title{position:absolute;top:250px;width:1200px;text-align:center;font-size:64px;font-weight:600;color:var(--blue-deep);letter-spacing:.08em}
.hero-lead{position:absolute;top:360px;width:1200px;text-align:center;font-size:13px;line-height:2;color:var(--blue)}

/* about */
.about{position:absolute;top:600px;left:0;width:1200px;height:420px;background:linear-gradient(90deg,#f4f8fb,#e2eef5)}
.about-photo{position:absolute;left:720px;top:20px;width:300px;height:400px;background:linear-gradient(160deg,#dbe8f0,#b7cbd9 60%,#9db4c6)}
.section-label{font-family:"Noto Serif JP",serif;font-style:italic;font-size:22px;color:var(--blue)}
.about .section-label{position:absolute;left:380px;top:36px}
.about-heading{position:absolute;left:250px;top:86px;width:380px;text-align:center;font-size:24px;line-height:1.6;color:var(--blue-deep)}
.about-text{position:absolute;left:220px;top:186px;width:440px;font-size:12px;line-height:2.1;color:var(--muted)}
.about-sign{position:absolute;left:380px;top:380px;font-size:12px;color:var(--ink)}

/* cycle */
.cycle-heading{position:absolute;left:60px;top:1050px;font-size:28px;line-height:1.55;font-weight:700;color:var(--ink)}
.cycle-text{position:absolute;left:60px;top:1146px;width:640px;font-size:12px;line-height:1.9;color:var(--muted)}
.cycle-diagram{position:absolute;left:180px;top:1160px}
.cycle-tagline{position:absolute;top:1392px;width:1200px;text-align:center;font-family:"Lato",sans-serif;font-style:italic;font-weight:700;font-size:24px;color:var(--blue)}

/* service */
.service{position:absolute;top:1450px;left:0;width:1200px;height:470px;background:linear-gradient(180deg,#9ad2e1,#7ec2d6)}
.service .section-label{position:absolute;top:40px;width:1200px;text-align:center;color:var(--white);font-size:26px}
.service-card{position:absolute;top:108px;width:250px}
.service-photo{width:250px;height:130px;background:linear-gradient(135deg,#e8eef2,#b9c9d4)}
.service-title{margin-top:16px;text-align:center;font-size:17px;font-weight:700;color:var(--white);font-family:"Noto Serif JP",serif}
.service-sub{text-align:center;font-family:"Lato",sans-serif;font-size:10px;color:rgba(255,255,255,.85);margin-top:2px}
.service-text{margin-top:12px;font-size:11px;line-height:1.9;color:var(--white);text-align:center}
.service .btn-more{top:384px;width:130px;height:30px}

/* member */
.member-title{position:absolute;top:1966px;width:1200px;text-align:center;font-size:26px;color:var(--muted)}
.member-photo{position:absolute;top:2040px;width:300px;height:440px}
.member-photo.is-featured{top:2024px;height:476px;box-shadow:0 6px 18px rgba(0,0,0,.2);z-index:2}
.member-caption{position:absolute;left:0;bottom:0;width:300px;height:90px;background:rgba(44,127,179,.88);color:var(--white);text-align:center;padding-top:18px}
.member-role{font-family:"Lato",sans-serif;font-size:10px;letter-spacing:.1em}
.member-name{font-family:"Noto Serif JP",serif;font-size:24px;margin-top:4px}

/* news & blog */
.feed{position:absolute;top:2540px;width:500px}
.feed-title{font-family:"Noto Serif JP",serif;font-size:22px;color:var(--ink);padding-bottom:10px;border-bottom:2px solid var(--blue)}
.feed-list{list-style:none}
.feed-list li{padding:13px 0;border-bottom:1px solid var(--line)}
.feed-date{font-family:"Lato",sans-serif;font-size:10px;color:var(--blue)}
.feed-text{font-size:11px;color:var(--ink);margin-top:2px}

/* recruit */
.recruit{position:absolute;top:3010px;left:0;width:1200px;height:400px;background:linear-gradient(180deg,#6fb3cf,#9ccbdd 60%,#c8e0ea)}
.recruit-label{position:absolute;top:80px;width:1200px;text-align:center;font-family:"Noto Serif JP",serif;font-style:italic;font-size:18px;color:var(--white)}
.recruit-heading{position:absolute;top:118px;width:1200px;text-align:center;font-size:28px;font-weight:600;color:var(--white)}
.recruit-text{position:absolute;top:184px;width:1200px;text-align:center;font-size:11px;line-height:1.8;color:var(--white)}
.recruit .btn-more{left:520px;top:268px}

/* footer */
.site-footer{position:absolute;top:3410px;left:0;width:1200px;height:282px;background:var(--white)}
.footer-brand{position:absolute;left:60px;top:70px;display:flex;align-items:center;gap:10px}
.footer-address{position:absolute;left:60px;top:118px;font-size:9px;line-height:1.7;color:var(--muted)}
.footer-nav{position:absolute;top:66px;display:flex;flex-direction:column;gap:2px;font-family:"Lato",sans-serif;font-size:9px;color:var(--muted)}
.footer-nav b{color:var(--ink);font-size:10px}
.site-footer .btn-contact{left:1030px;top:72px}
.copyright{position:absolute;left:0;bottom:0;width:1200px;height:26px;background:#eef2f5;font-family:"Lato",sans-serif;font-size:9px;color:var(--muted);display:flex;align-items:center;justify-content:center}
</style>
</head>
<body>

<header class="site-header">
  <div class="brand"><span class="brand-dot"></span><span class="brand-name">ルミエラ</span></div>
  <nav class="global-nav">
    <a class="is-active">Home</a><a>About Us</a><a>Service</a><a>Member</a><a>News</a><a>Blog</a>
  </nav>
  <div class="btn-contact">Contact</div>
</header>

<section class="hero" role="img" aria-label="やわらかな色の光の玉が浮かぶ背景">
  <h1 class="hero-title serif">AI人材が育つ</h1>
  <p class="hero-lead">ディープラーニングの基礎からアプリケーション開発までを丁寧にサポートし、<br>次世代のAI人材を育成する学びの場をつくります。</p>
  <div class="btn-more" style="left:520px;top:494px">MORE</div>
</section>

<section class="about">
  <div class="about-photo" role="img" aria-label="スーツ姿の代表者の写真"></div>
  <h2 class="section-label">About Us</h2>
  <p class="about-heading serif">人と人とが教えあえる<br>やさしい世界を作る</p>
  <p class="about-text">私たちは「学ぶ楽しさ」を大切にしながら、人工知能の知識をわかりやすく届けることを使命としています。難しく見える技術も、順を追って理解すれば誰にでも扱えるものです。受講者一人ひとりに寄り添い、現場で役立つ力を身につけていただけるよう、講師と受講者がともに成長できる環境づくりに取り組んでいます。教える人と学ぶ人がつながり、その輪が社会へ広がっていく未来を目指します。</p>
  <p class="about-sign">株式会社ルミエラ　代表取締役社長　宮本 誠</p>
</section>

<h2 class="cycle-heading serif">人工知能（AI）における教育と<br>コンサルティングサービスを提供</h2>
<p class="cycle-text">目標設定から課題の整理、学習モデルの構築、現場への取り込みまでを一貫してサポートします。</p>

<svg class="cycle-diagram" width="840" height="230" viewBox="0 15 840 230">
  <g fill="none" stroke-width="26">
    <circle cx="420" cy="130" r="80" stroke="var(--do)" stroke-dasharray="125.6 377" transform="rotate(-90 420 130)"/>
    <circle cx="420" cy="130" r="80" stroke="var(--check)" stroke-dasharray="125.6 377" transform="rotate(0 420 130)"/>
    <circle cx="420" cy="130" r="80" stroke="var(--action)" stroke-dasharray="125.6 377" transform="rotate(90 420 130)"/>
    <circle cx="420" cy="130" r="80" stroke="var(--plan)" stroke-dasharray="125.6 377" transform="rotate(180 420 130)"/>
  </g>
  <g stroke-width="2" fill="none">
    <path d="M185 70 H330 L360 80" stroke="var(--plan)"/>
    <path d="M655 70 H510 L480 80" stroke="var(--do)"/>
    <path d="M185 190 H330 L360 180" stroke="var(--action)"/>
    <path d="M655 190 H510 L480 180" stroke="var(--check)"/>
  </g>
  <g font-family="Lato,sans-serif" font-weight="700" font-size="20">
    <circle cx="230" cy="40" r="20" fill="var(--plan)"/><text x="230" y="47" fill="#fff" text-anchor="middle">1</text>
    <text x="185" y="62" fill="var(--plan)" text-anchor="end">PLAN</text>
    <text x="185" y="90" fill="var(--ink)" font-size="12" font-family="Noto Sans JP,sans-serif" text-anchor="end">目標</text>
    <circle cx="610" cy="40" r="20" fill="var(--do)"/><text x="610" y="47" fill="#fff" text-anchor="middle">2</text>
    <text x="655" y="62" fill="var(--do)">DO</text>
    <text x="655" y="90" fill="var(--ink)" font-size="12" font-family="Noto Sans JP,sans-serif">課題設定</text>
    <circle cx="230" cy="160" r="20" fill="var(--action)"/><text x="230" y="167" fill="#fff" text-anchor="middle">4</text>
    <text x="185" y="182" fill="var(--action)" text-anchor="end">ACTION</text>
    <text x="185" y="210" fill="var(--ink)" font-size="12" font-family="Noto Sans JP,sans-serif" text-anchor="end">取り込み</text>
    <circle cx="610" cy="160" r="20" fill="var(--check)"/><text x="610" y="167" fill="#fff" text-anchor="middle">3</text>
    <text x="655" y="182" fill="var(--check)">CHECK</text>
    <text x="655" y="210" fill="var(--ink)" font-size="12" font-family="Noto Sans JP,sans-serif">学習モデル構築</text>
  </g>
</svg>
<p class="cycle-tagline">We provide education in the best style for you.</p>

<section class="service">
  <h2 class="section-label">Service</h2>
  <div class="service-card" style="left:200px">
    <div class="service-photo" role="img" aria-label="セミナー受講の様子の写真"></div>
    <p class="service-title">法人向けセミナー</p><p class="service-sub">Corporate Seminar</p>
    <p class="service-text">企業の現場で活かせるAI活用の<br>基礎から応用までを学べます。</p>
  </div>
  <div class="service-card" style="left:475px">
    <div class="service-photo" role="img" aria-label="講義を受ける受講者の写真"></div>
    <p class="service-title">個人向けセミナー</p><p class="service-sub">Personal Seminar</p>
    <p class="service-text">初めての方でも安心して<br>機械学習を学べる講座です。</p>
  </div>
  <div class="service-card" style="left:750px">
    <div class="service-photo" role="img" aria-label="打ち合わせをするビジネスパーソンの写真"></div>
    <p class="service-title">コンサルティング事業</p><p class="service-sub">Consulting</p>
    <p class="service-text">課題の整理からモデル構築まで<br>導入を一貫して支援します。</p>
  </div>
  <div class="btn-more is-light" style="left:260px">MORE</div>
  <div class="btn-more is-light" style="left:535px">MORE</div>
  <div class="btn-more is-light" style="left:810px">MORE</div>
</section>

<h2 class="member-title serif">Member</h2>
<div class="member-photo" style="left:0;background:linear-gradient(180deg,#eef1f3,#c7ced4)" role="img" aria-label="メンバーの人物写真"></div>
<div class="member-photo is-featured" style="left:300px;background:linear-gradient(180deg,#e5edf2,#b8c6d0)" role="img" aria-label="講師の人物写真">
  <div class="member-caption"><p class="member-role">Chief Learning Officer</p><p class="member-name">青木 航平</p></div>
</div>
<div class="member-photo" style="left:600px;background:linear-gradient(180deg,#edf0f2,#c3cbd2)" role="img" aria-label="メンバーの人物写真"></div>
<div class="member-photo" style="left:900px;background:linear-gradient(180deg,#f0f2f4,#c9d0d6)" role="img" aria-label="メンバーの人物写真"></div>

<section class="feed" style="left:80px">
  <h2 class="feed-title">News</h2>
  <ul class="feed-list">
    <li><p class="feed-date">2017.02.01</p><p class="feed-text">春季AIセミナーの受講者募集を開始しました</p></li>
    <li><p class="feed-date">2017.01.24</p><p class="feed-text">法人向け機械学習研修の新コースを公開しました</p></li>
    <li><p class="feed-date">2017.01.16</p><p class="feed-text">オンライン講座の受講者数が一万人を突破しました</p></li>
    <li><p class="feed-date">2017.01.05</p><p class="feed-text">年始の営業日についてのお知らせ</p></li>
    <li><p class="feed-date">2016.12.20</p><p class="feed-text">ディープラーニング入門講座を開催しました</p></li>
    <li><p class="feed-date">2016.12.08</p><p class="feed-text">新しいメンバーが加わりました</p></li>
  </ul>
</section>
<section class="feed" style="left:620px">
  <h2 class="feed-title">Blog</h2>
  <ul class="feed-list">
    <li><p class="feed-date">2017.02.03</p><p class="feed-text">数学が苦手でも機械学習は学べるのか</p></li>
    <li><p class="feed-date">2017.01.27</p><p class="feed-text">講師が語る「教える」ということ</p></li>
    <li><p class="feed-date">2017.01.19</p><p class="feed-text">画像認識モデルを手軽に試す方法</p></li>
    <li><p class="feed-date">2017.01.10</p><p class="feed-text">受講者インタビュー：現場での活用事例</p></li>
    <li><p class="feed-date">2016.12.22</p><p class="feed-text">今年のAI業界を振り返って</p></li>
    <li><p class="feed-date">2016.12.12</p><p class="feed-text">はじめてのPython環境構築</p></li>
  </ul>
</section>

<section class="recruit" role="img" aria-label="ネットワークが重なる都市の風景写真">
  <p class="recruit-label">Recruit</p>
  <h2 class="recruit-heading serif">共に学び、共に育つ仲間を求めています</h2>
  <p class="recruit-text">人工知能の教育を通じて社会を変えていく挑戦に、<br>一緒に取り組んでくださる方を募集しています。</p>
  <div class="btn-more is-light">MORE</div>
</section>

<footer class="site-footer">
  <div class="footer-brand"><span class="brand-dot"></span><span class="brand-name">ルミエラ</span></div>
  <p class="footer-address">株式会社ルミエラ<br>東京都青葉区みなと町1-2-3</p>
  <div class="footer-nav" style="left:560px"><b>About Us</b><span>Message</span><span>Company</span><span>Access</span></div>
  <div class="footer-nav" style="left:680px"><b>Service</b><span>Corporate</span><span>Personal</span><span>Consulting</span></div>
  <div class="footer-nav" style="left:800px"><b>Member</b><b>News</b><b>Blog</b><b>Recruit</b></div>
  <div class="btn-contact">Contact</div>
  <div class="copyright">Copyright © Lumiera Inc. All Rights Reserved.</div>
</footer>

</body>
</html>
```